App Screenshots

We need professional looking screenshots for out apps Thought Arena and Thought Arena Plus.
The screenshots should incorporate text highlighting features or other significant details.
You can see the current screenshots here:
https://apps.example-store.test/details?id=cerebrix.thoughtarena
And here is some of our competition.
Neuro Duels:
https://apps.example-store.test/details?id=kr.co.velquora.neuroduels
Cognivane
https://apps.example-store.test/details?id=com.ferrinworks.cognivane
Some example to use in the screenshots:
Thought Arena "exercise your brain"
Used by over 8 million people
Nearly three dozen brain training games to challenge you daily
Discover your strengths and weaknesses
Exercise a broad range of cognitive skills
Based on principles of cognitive psychology
For the pro version, text can also be added:
The training center selects games for you based on your strengths and weaknesses
The text doesn't have to be exactly the same if you can think of something better, or need to modify it to fit.
We need the ability to modify the text and insert different screenshots into the images. This will allow us to modify them for multiple languages. PSD files preferred. Raw screenshots are attached for convenience.

```html
<!DOCTYPE html>
<html lang="en">
<head>
<meta charset="utf-8">
<title>Thought Arena – Used by over 8 million people</title>
<link href="https://fonts.googleapis.com/css2?family=Montserrat:wght@700;800&family=Roboto:ital,wght@0,500;0,700;1,700&display=swap" rel="stylesheet">
<style>
  :root{
    --sky:#2f8ee6;
    --sky-light:#4aa3f0;
    --white:#ffffff;
    --phone:#1b1b1d;
    --phone-edge:#3a3a3d;
    --navy:#2b3a6b;
    --bar-navy:#14238f;
    --bar-track:#9a9a9a;
    --list-bg:#d9d9d9;
    --strip:#ee1c5c;
    --pro:#ffd21f;
    --purple:#6a1b82;
    --pink:#ea1e63;
    --red:#ef2d2d;
    --cyan:#1aa3d9;
    --ink:#111111;
  }
  *{margin:0;padding:0;box-sizing:border-box}
  html,body{width:677px;height:1200px;overflow:hidden}
  body{position:relative;background:linear-gradient(160deg,var(--sky-light) 0%,var(--sky) 45%,var(--sky) 100%);font-family:"Roboto",sans-serif}
  .headline{position:absolute;left:0;top:0;width:677px;color:var(--white);font-family:"Montserrat",sans-serif;font-weight:800}
  .headline__lead{position:absolute;top:34px;width:100%;text-align:center;font-size:62px;letter-spacing:1px}
  .headline__figure{position:absolute;left:108px;top:82px;font-size:178px;line-height:1}
  .headline__unit{position:absolute;left:248px;top:92px;font-size:90px;line-height:1;letter-spacing:2px}
  .headline__people{position:absolute;left:252px;top:188px;font-size:40px;font-weight:700;letter-spacing:27px}

  .phone{position:absolute;left:40px;top:338px;width:597px;height:940px;background:var(--phone);border-radius:70px;border:3px solid var(--phone-edge)}
  .phone__speaker{position:absolute;left:249px;top:55px;width:100px;height:12px;border-radius:6px;background:#2e2e31}
  .phone__camera{position:absolute;left:198px;top:52px;width:18px;height:18px;border-radius:50%;background:#2e2e31}
  .screen{position:absolute;left:39px;top:142px;width:526px;height:800px;background:var(--list-bg);overflow:hidden}
  .appbar{height:110px;background:var(--navy);border-bottom:4px solid #1e2a52;display:flex;align-items:center;justify-content:center;position:relative}
  .appbar__back{position:absolute;left:20px;top:26px}
  .appbar__title{color:var(--white);font-weight:700;font-size:60px}

  .game{position:absolute;left:12px;width:502px;height:172px;background:var(--white);border-radius:14px;overflow:hidden}
  .game__icon{position:absolute;left:10px;top:12px;width:130px;height:130px;border-radius:50%}
  .game__name{position:absolute;left:150px;top:10px;width:340px;text-align:center;font-weight:700;font-size:19px;color:var(--ink)}
  .game__label{position:absolute;left:150px;top:50px;width:340px;text-align:center;font-weight:700;font-size:18px;color:var(--bar-navy)}
  .game__bar{position:absolute;left:155px;top:75px;width:336px;height:26px;border-radius:13px;background:var(--bar-track);overflow:hidden}
  .game__fill{height:100%;background:var(--bar-navy);border-radius:13px;border:2px solid #0a1460;color:var(--white);font-weight:700;font-size:19px;display:flex;align-items:center;justify-content:center}
  .game__strip{position:absolute;left:0;bottom:0;width:100%;height:26px;background:var(--strip);display:flex;align-items:center;justify-content:space-between;padding:0 16px 0 150px}
  .game__category{color:var(--white);font-weight:700;font-style:italic;font-size:18px;flex:1;text-align:center}
  .game__pro{color:var(--pro);font-weight:700;font-style:italic;font-size:19px}
</style>
</head>
<body>
  <header class="headline">
    <div class="headline__lead">USED BY OVER</div>
    <div class="headline__figure">8</div>
    <div class="headline__unit">MILLION</div>
    <div class="headline__people">PEOPLE</div>
  </header>

  <div class="phone">
    <div class="phone__camera"></div>
    <div class="phone__speaker"></div>
    <div class="screen">
      <div class="appbar">
        <svg class="appbar__back" width="34" height="58" viewBox="0 0 34 58"><path d="M30 4 L6 29 L30 54" fill="none" stroke="#fff" stroke-width="6" stroke-linecap="round" stroke-linejoin="round"/></svg>
        <div class="appbar__title">Games</div>
      </div>

      <div class="game" style="top:121px">
        <div class="game__icon" role="img" aria-label="Memory Match game icon" style="background:var(--purple)"></div>
        <div class="game__name">Memory Match</div>
        <div class="game__label">Percentile:</div>
        <div class="game__bar"><div class="game__fill" style="width:91%">Best: 97</div></div>
        <div class="game__strip"><span class="game__category">Learning Strategy</span><span class="game__pro">Pro</span></div>
      </div>

      <div class="game" style="top:302px">
        <div class="game__icon" role="img" aria-label="Self-Ordered Learning for Objects game icon" style="background:var(--pink)"></div>
        <div class="game__name">Self-Ordered Learning for Objects</div>
        <div class="game__label">Percentile:</div>
        <div class="game__bar"><div class="game__fill" style="width:72%">Best: 73</div></div>
        <div class="game__strip"><span class="game__category">Learning Strategy</span><span class="game__pro">Pro</span></div>
      </div>

      <div class="game" style="top:483px">
        <div class="game__icon" role="img" aria-label="Anticipation game icon" style="background:var(--red)"></div>
        <div class="game__name">Anticipation</div>
        <div class="game__label">Percentile:</div>
        <div class="game__bar"><div class="game__fill" style="width:100%">Best: 99</div></div>
        <div class="game__strip"><span class="game__category">Divided Attention</span><span class="game__pro">Pro</span></div>
      </div>

      <div class="game" style="top:664px">
        <div class="game__icon" role="img" aria-label="Divided Attention game icon" style="background:var(--cyan)"></div>
        <div class="game__name">Divided Attention Level 1</div>
      </div>
    </div>
  </div>
</body>
</html>
```